IT Services

We come to you
Only $49/hr
No contract, no monthly fee
Software engineer on staff
remote assistance or visit in your office

On the back of the card I want to list services.

- Server setup
- Network troubleshooting
- Printer setup
- Secure backup setup
- Software installation
- Wireless network setup
- Wired network setup
- Disaster recovery
- Website management
- Any other technology related support
- Email setup
- HIPAA compliance review and setup
Updates

the URL is: GEARFIXPRO.ZONE please use it on the card

On the card we need to mention "Connect remotely to address your IT issues" if there is enough room as well as "we go to you"

Industry/Entity Type

Printer

Contact Information for Business Card

I want a busoiness card to offer my services to doctor offices, it can be dentists, Otamatry, and other professions. I provide the following service. My plan is to go to their office and drop off my card. I don't want them to forget about it that is why I am paying for the design. I like hand writing design formats.

```html
<!DOCTYPE html>
<html lang="en">
<head>
<meta charset="utf-8">
<title>GEARFIXPRO.ZONE – IT Services Business Card</title>
<link rel="stylesheet" href="https://fonts.googleapis.com/css2?family=Kalam:wght@400;700&family=Permanent+Marker&display=swap">
<style>
  :root {
    --backdrop: #2b2b2b;
    --card: #f4f4f4;
    --card-edge: #e2e2e2;
    --ink: #111111;
    --ink-soft: #6a6a6a;
    --sketch-tone: #dcdcdc;
  }
  * { box-sizing: border-box; margin: 0; padding: 0; }
  html, body {
    width: 1200px;
    height: 900px;
    overflow: hidden;
    background: var(--backdrop);
  }
  .stage {
    position: relative;
    width: 1200px;
    height: 900px;
  }
  .card {
    position: absolute;
    width: 525px;
    height: 300px;
    background: linear-gradient(160deg, #ffffff 0%, var(--card) 60%, var(--card-edge) 100%);
    border-radius: 16px;
    box-shadow: 0 10px 24px rgba(0,0,0,0.45);
    overflow: hidden;
  }
  .card--front { left: 50px; top: 160px; }
  .card--back  { left: 625px; top: 440px; }

  .pitch {
    position: absolute;
    left: 24px;
    top: 92px;
    width: 190px;
    font-family: "Kalam", cursive;
    font-size: 14px;
    line-height: 1.25;
    color: var(--ink);
    text-align: center;
    list-style: none;
  }
  .network-sketch {
    position: absolute;
    right: 22px;
    top: 18px;
    width: 285px;
    height: 190px;
    border-radius: 8px;
    background: radial-gradient(ellipse at center, var(--sketch-tone) 0%, rgba(220,220,220,0) 75%);
  }
  .site-url {
    position: absolute;
    left: 0;
    right: 0;
    font-family: "Permanent Marker", cursive;
    font-size: 28px;
    letter-spacing: 1px;
    color: var(--ink);
    text-align: center;
  }
  .card--front .site-url { bottom: 26px; padding-left: 20px; }
  .card--back .site-url { bottom: 30px; }

  .services {
    position: absolute;
    left: 30px;
    right: 30px;
    top: 40px;
    font-family: "Kalam", cursive;
    font-size: 17px;
    line-height: 1.3;
    color: var(--ink-soft);
    text-align: center;
    list-style: none;
  }
  .services li::before { content: "○ "; font-size: 13px; }
  .services li { display: inline; margin: 0 6px; }
  .services .row { display: block; }
</style>
</head>
<body>
  <main class="stage">
    <section class="card card--front" aria-label="Card front">
      <ul class="pitch">
        <li>We come to you</li>
        <li>Only $49/hr</li>
        <li>No contract, no monthly fee</li>
        <li>Software engineer on staff</li>
        <li>remote assistance or visit in your office</li>
      </ul>
      <div class="network-sketch" role="img" aria-label="Hand-drawn sketch of a small office network: internet cloud, router, phone, printer, laptop, firewall, server and desktop joined by arrows"></div>
      <p class="site-url">WWW.GEARFIXPRO.ZONE</p>
    </section>

    <section class="card card--back" aria-label="Card back">
      <div class="services">
        <span class="row"><li>Server setup</li><li>Network troubleshooting</li></span>
        <span class="row"><li>Printer setup</li><li>Secure backup setup</li></span>
        <span class="row"><li>Software installation</li><li>Wireless network setup</li></span>
        <span class="row"><li>Wired network setup</li><li>Disaster recovery</li></span>
        <span class="row"><li>Website management</li><li>Any other technology</li></span>
        <span class="row">related support <li>Email setup</li></span>
        <span class="row"><li>HIPAA compliance review and setup</li></span>
      </div>
      <p class="site-url">WWW.GEARFIXPRO.ZONE</p>
    </section>
  </main>
</body>
</html>
```